Brisk Vantage Webpage

Brisk Vantag need a simple, elegant and professional website

As the company is selling products and clothes for companies we would like to have a large picture carousel on the top.
As one of the logos have black background I would like the webpage to be black.

There should also be thre boxes on main page where we can have information about the product of the month, news and other.

On the menu we need:
- Our products
-our catalogues (here we need to have the possibility to upload several pdf and e-catalogues
-About us
-Contact us
-News

Here are som pages in the same branch
http://www.kelmarwear.example/
http://www.trudelo.example/
http://www.varnistack.example/

I will attach the logo with both white and black background.
The logos are attached in png but I have eps and jpg as well. Just let me know what you need.

looking forward to your designs:)

Brisk Vantage is a company that provides corporate profile products such as logo on t-shirts, work uniform, pens, cups etc. We also work with event companies that need advertising and profile products for theirs event as well as the sports segment.

Target Market(s)

corporate, eventcompanies and sportsegment

Industry/Entity Type

Advertising

Requirements
Must have
• Facebook, twitter and like button for social media

```html
<!DOCTYPE html>
<html lang="en">
<head>
<meta charset="utf-8">
<title>Brisk Vantag</title>
<link rel="stylesheet" href="https://fonts.googleapis.com/css2?family=Bebas+Neue&family=Lato:wght@400;700&family=Pathway+Gothic+One&family=Oswald:wght@600&display=swap">
<style>
:root{
  --black:#000;
  --brand-blue:#1e9be0;
  --deep-blue:#0b5b9c;
  --light-blue:#7ec8f0;
  --orange:#f7941d;
  --nav-top:#f7f7f7;
  --nav-bottom:#d9d9d9;
  --nav-text:#555;
  --card-grey:#e6e7e8;
  --title-grey:#4a4a4a;
  --footer-bg:#222;
  --footer-line:#444;
  --footer-text:#c8c8c8;
}
*{margin:0;padding:0;box-sizing:border-box}
html,body{width:1200px;height:1126px;overflow:hidden;background:#fff}
body{position:relative;font-family:"Lato",sans-serif}

.site-header{position:absolute;left:0;top:0;width:1200px;height:110px;background:var(--black)}
.brand{position:absolute;left:440px;top:20px;display:flex;align-items:center;gap:12px}
.brand-dot{width:72px;height:72px;border-radius:50%;background:#fff}
.brand-name{font-family:"Bebas Neue",sans-serif;font-size:52px;color:var(--brand-blue);line-height:72px;letter-spacing:1px}
.follow{position:absolute;left:901px;top:55px;display:flex;align-items:center;gap:6px}
.follow-label{font-family:"Oswald",sans-serif;font-weight:600;font-size:12px;color:var(--orange);margin-right:6px}
.social-square{width:18px;height:18px;background:#4a6fa5}
.social-square.alt{background:#4fb3e8}

.main-nav{position:absolute;left:0;top:110px;width:1200px;height:47px;background:linear-gradient(var(--nav-top),var(--nav-bottom));border-top:1px solid #fff}
.search{position:absolute;left:131px;top:9px;width:338px;height:29px;background:#fff;border:1px solid #ccc;display:flex;align-items:center;padding-left:10px;gap:8px}
.search-text{font-family:"Pathway Gothic One",sans-serif;font-style:italic;font-size:16px;color:#999;letter-spacing:.5px}
.menu{position:absolute;left:480px;top:0;height:46px;display:flex;list-style:none;border-left:1px solid #bbb}
.menu li{height:46px;border-right:1px solid #bbb;font-family:"Pathway Gothic One",sans-serif;font-size:20px;color:var(--nav-text);line-height:46px;text-align:center}

.hero{position:absolute;left:0;top:157px;width:1200px;height:305px}
.hero-photo{position:absolute;inset:0;background:radial-gradient(ellipse at 50% 40%,#6e7478 0%,#3a3e42 45%,#111 100%)}
.hero-arrow{position:absolute;top:136px}
.hero-copy{position:absolute;left:657px;top:52px;width:320px;text-align:center;color:#fff}
.hero-kicker{font-family:"Bebas Neue",sans-serif;font-size:34px;line-height:34px;color:var(--light-blue)}
.hero-title{font-family:"Bebas Neue",sans-serif;font-size:56px;line-height:50px}
.hero-sub{font-family:Arial,sans-serif;font-size:14px;margin-top:4px}
.btn-blue{display:inline-block;background:linear-gradient(#2a8ae0,#0a4fb0);color:#fff;font-family:"Bebas Neue",sans-serif;text-align:center}
.hero-btn{width:120px;height:42px;line-height:44px;font-size:24px;margin-top:13px}

.feature{position:absolute;top:497px;width:290px;height:316px;background:var(--card-grey);text-align:center}
.feature.highlight{background:var(--deep-blue)}
.feature-photo{position:absolute;left:21px;top:13px;width:250px;height:116px;border:4px solid #f4f4f4;box-shadow:0 4px 5px rgba(0,0,0,.35)}
.feature-title{position:absolute;left:0;top:150px;width:290px;font-family:"Bebas Neue",sans-serif;font-size:27px;color:var(--title-grey)}
.feature.highlight .feature-title{color:#fff}
.feature-text{position:absolute;left:21px;top:186px;width:255px;text-align:left;font-size:12px;line-height:16px;color:#222}
.feature.highlight .feature-text{color:#fff}
.feature-btn{position:absolute;left:92px;top:253px;width:106px;height:38px;line-height:40px;font-size:21px;color:#fff;font-family:"Bebas Neue",sans-serif}
.btn-dark{background:linear-gradient(#555,#111)}

.site-footer{position:absolute;left:0;top:862px;width:1200px;height:264px;background:repeating-linear-gradient(90deg,#232323 0 2px,#1f1f1f 2px 4px)}
.footer-col{position:absolute;top:32px}
.footer-heading{font-family:"Pathway Gothic One",sans-serif;font-size:27px;color:var(--brand-blue);padding-left:22px;height:39px}
.footer-list{list-style:none;border-top:1px solid var(--footer-line)}
.footer-list li{height:31px;line-height:31px;border-bottom:1px solid var(--footer-line);font-size:13px;color:var(--footer-text);padding-left:20px;position:relative}
.footer-list li::before{content:"";position:absolute;left:4px;top:14px;border-left:4px solid #555;border-top:3px solid transparent;border-bottom:3px solid transparent}
.date{color:var(--orange)}
.copyright{color:var(--brand-blue)}
</style>
</head>
<body>
<header class="site-header">
  <div class="brand"><span class="brand-dot"></span><span class="brand-name">Brisk Vantag</span></div>
  <div class="follow"><span class="follow-label">Follow Brisk Vantag</span><span class="social-square"></span><span class="social-square alt"></span></div>
</header>

<nav class="main-nav">
  <div class="search">
    <svg width="16" height="16" viewBox="0 0 16 16"><circle cx="6.5" cy="6.5" r="5" fill="none" stroke="#666" stroke-width="1.6"/><line x1="10" y1="10" x2="15" y2="15" stroke="#666" stroke-width="1.8"/></svg>
    <span class="search-text">What are you looking for?</span>
  </div>
  <ul class="menu">
    <li style="width:140px">Our products</li>
    <li style="width:138px">Our catalogues</li>
    <li style="width:105px">About us</li>
    <li style="width:114px">Contact us</li>
    <li style="width:83px">News</li>
  </ul>
</nav>

<section class="hero">
  <div class="hero-photo" role="img" aria-label="Two athletes in sports jackets against a stormy sky with splashing water"></div>
  <svg class="hero-arrow" style="left:47px" width="18" height="30" viewBox="0 0 18 30"><polyline points="15,2 3,15 15,28" fill="none" stroke="#777" stroke-width="3"/></svg>
  <svg class="hero-arrow" style="left:1134px" width="18" height="30" viewBox="0 0 18 30"><polyline points="3,2 15,15 3,28" fill="none" stroke="#1e9be0" stroke-width="3"/></svg>
  <div class="hero-copy">
    <div class="hero-kicker">Lorem ipsum dolor</div>
    <div class="hero-title">Seledent<br>Amor et lesd</div>
    <div class="hero-sub">Lorem ipsum dolor et se le delerent</div>
    <span class="btn-blue hero-btn">Learn more</span>
  </div>
</section>

<article class="feature highlight" style="left:142px">
  <div class="feature-photo" role="img" aria-label="Two models in blue sportswear on a night street" style="background:linear-gradient(90deg,#3a4a6a,#b07a3a,#2a3550)"></div>
  <h2 class="feature-title">Product of the month</h2>
  <p class="feature-text">Lorem ipsum dolor et me mensaje del a la nula estaba en la dolor.&nbsp; No em mehidian delibah meiserelifereba en tu model.</p>
  <span class="feature-btn btn-blue">Read more</span>
</article>

<article class="feature" style="left:454px">
  <div class="feature-photo" role="img" aria-label="Woman training with a weight plate in a gym" style="background:linear-gradient(90deg,#d8d8d8,#8a8a8a,#c4c4c4)"></div>
  <h2 class="feature-title">News</h2>
  <p class="feature-text">Lorem ipsum dolor et me mensaje del a la nula estaba en la dolor.&nbsp; No em mehidian delibah meiserelifereba en tu model.</p>
  <span class="feature-btn btn-dark">Read more</span>
</article>

<article class="feature" style="left:768px">
  <div class="feature-photo" role="img" aria-label="Two people doing a fitness workout in a studio" style="background:linear-gradient(#b8aea0,#8a6a4a)"></div>
  <h2 class="feature-title">Other</h2>
  <p class="feature-text">Lorem ipsum dolor et me mensaje del a la nula estaba en la dolor.&nbsp; No em mehidian delibah meiserelifereba en tu model.</p>
  <span class="feature-btn btn-dark">Read more</span>
</article>

<footer class="site-footer">
  <div class="footer-col" style="left:142px;width:189px">
    <h3 class="footer-heading">LINKS</h3>
    <ul class="footer-list">
      <li>Our products</li><li>Our catalogues</li><li>About us</li><li>Contact us</li><li>News</li>
    </ul>
  </div>
  <div class="footer-col" style="left:383px;width:399px">
    <h3 class="footer-heading">LATEST NEWS</h3>
    <ul class="footer-list">
      <li>Lorem ipsun dolor et mest et lerbare&nbsp; et&nbsp; <span class="date">(20/04/2013)</span></li>
      <li>Lorem ipsun dolor et mest et lerbare&nbsp; et el lap ter&nbsp; <span class="date">(20/04/2013)</span></li>
      <li>Lorem ipsun dolor et mest&nbsp; <span class="date">(20/04/2013)</span></li>
      <li>Lorem ipsun dolor et mest et lerbare&nbsp; et&nbsp; <span class="date">(20/04/2013)</span></li>
      <li>Lorem ipsun dolor et mest et lerbare lebrareista&nbsp; et&nbsp; <span class="date">(20/04/2013)</span></li>
    </ul>
  </div>
  <div class="footer-col" style="left:824px;width:234px">
    <h3 class="footer-heading">CONTACT US</h3>
    <ul class="footer-list">
      <li>Torvel gate 9 Brennvik / Norway</li>
      <li>Telf: 55 01 23 45</li>
      <li>Fax:&nbsp; 55 01 23 45</li>
      <li>mail@briskvantag.example</li>
      <li class="copyright">copyright © 2013 | Brisk Vantag</li>
    </ul>
  </div>
</footer>
</body>
</html>
```